Legal Postcard for Carlvista Film Works

LEGAL VIDEO SERVICES- Expert & Lay Witness Depositions- Day in the Life Videos- Security & Surveillance Video Editing- Onsite Video Documentation- Ability to make bad video clearer- Focus Groups & Video Monitoring- Video Conversion and Duplication- Over 15 Years of Legal Video Experience

Phone: 418.562.7391
Email: Walter@Carlvista.example

Target Market(s)

Law Firms

Industry/Entity Type

Legal

Font styles to use
Serif

Requirements
Must have
• The information in my description, my logo & picture.
• Nice design touches and accents
• Return address & Logo on mailing side of postcard, all other info on the main side
• Colors should be consistent with my logo

```html
<!DOCTYPE html>
<html lang="en">
<head>
<meta charset="utf-8">
<title>Carlvista Film Works – Legal Postcard</title>
<link rel="stylesheet" href="https://fonts.googleapis.com/css2?family=Open+Sans:wght@300;400;600&display=swap">
<style>
  :root {
    --page: #e9e9e9;
    --card: #ffffff;
    --brand-blue: #5260a8;
    --brand-blue-dark: #3f4c8f;
    --brand-grey: #8a8a8a;
    --grey-band: #9b9b9b;
    --rule: #c9c9c9;
    --ink: #4a4a4a;
    --light: #ffffff;
  }
  * { box-sizing: border-box; margin: 0; padding: 0; }
  html, body { width: 874px; height: 1200px; overflow: hidden; }
  body {
    background: var(--page);
    font-family: "Open Sans", Arial, sans-serif;
    position: relative;
  }
  .postcard {
    position: absolute;
    left: 60px;
    width: 754px;
    height: 470px;
    background: var(--card);
    box-shadow: 0 6px 18px rgba(0,0,0,.18);
    overflow: hidden;
  }
  .postcard--front { top: 110px; }
  .postcard--back { top: 640px; }

  /* Front */
  .front-field { position: absolute; inset: 0; }
  .experience-banner {
    position: absolute;
    left: 0; top: 22px;
    height: 40px;
    padding: 0 46px 0 26px;
    display: flex; align-items: center;
    color: var(--light);
    font-size: 17px; font-weight: 400;
    background: var(--brand-blue-dark);
    clip-path: polygon(0 0, 100% 0, calc(100% - 22px) 100%, 0 100%);
  }
  .hero-photo {
    position: absolute;
    right: 40px; top: 18px;
    width: 330px; height: 420px;
    background: radial-gradient(ellipse at 50% 45%, #b9b3ad 0%, #8c8681 45%, rgba(255,255,255,0) 72%);
  }
  .service-title {
    position: absolute;
    left: 26px; top: 110px;
    color: var(--light);
    font-size: 31px; font-weight: 300;
    letter-spacing: 2px; line-height: 1.2;
  }
  .service-list {
    position: absolute;
    left: 26px; top: 250px;
    list-style: none;
    color: var(--light);
    font-size: 14.5px; line-height: 1.45;
  }
  .service-list li::before { content: "• "; }
  .front-contacts {
    position: absolute;
    left: 26px; bottom: 22px;
    display: flex; gap: 28px;
    color: var(--light);
    font-size: 14px;
  }
  .contact { display: flex; align-items: center; gap: 7px; }
  .contact svg { width: 16px; height: 16px; }

  /* Back */
  .back-banner {
    position: absolute;
    left: 0; top: 26px;
    width: 350px; height: 40px;
    padding-left: 30px;
    display: flex; align-items: center;
    color: var(--light);
    font-size: 19px; font-weight: 300; letter-spacing: 2px;
    background: var(--brand-blue);
    clip-path: polygon(0 0, 100% 0, calc(100% - 24px) 100%, 0 100%);
  }
  .return-address {
    position: absolute;
    left: 388px; top: 26px;
    font-size: 13px; line-height: 1.35;
    color: var(--brand-grey);
  }
  .return-address .return-name { color: var(--brand-blue); font-weight: 600; }
  .stamp-box {
    position: absolute;
    right: 26px; top: 26px;
    width: 92px; height: 66px;
    border: 1px solid var(--rule);
  }
  .logo-mark {
    position: absolute;
    left: 30px; top: 110px;
    display: flex; align-items: center; gap: 10px;
    color: var(--brand-grey);
    font-size: 22px; font-weight: 600;
  }
  .logo-mark .dot { width: 18px; height: 18px; border-radius: 50%; background: var(--brand-grey); }
  .grey-band {
    position: absolute;
    left: 0; top: 232px;
    width: 368px; height: 84px;
    background: var(--grey-band);
    display: flex; align-items: center;
    padding-left: 30px;
    color: var(--light);
  }
  .band-name { font-size: 22px; font-weight: 300; width: 120px; }
  .band-contacts {
    border-left: 1px solid rgba(255,255,255,.7);
    padding-left: 16px;
    font-size: 13px; line-height: 1.9;
  }
  .web-band {
    position: absolute;
    left: 0; top: 328px;
    width: 368px; height: 40px;
    background: var(--brand-blue);
    color: var(--light);
    display: flex; align-items: center; justify-content: center;
    font-size: 18px; font-weight: 400;
  }
  .address-lines {
    position: absolute;
    left: 480px; top: 210px;
    width: 250px;
  }
  .address-lines span {
    display: block;
    height: 36px;
    border-bottom: 1px solid var(--rule);
  }
</style>
</head>
<body>

<section class="postcard postcard--front" aria-label="Postcard front">
  <svg class="front-field" viewBox="0 0 754 470" preserveAspectRatio="none" aria-hidden="true">
    <polygon points="0,78 360,78 470,470 0,470" fill="var(--brand-blue)"/>
  </svg>
  <div class="hero-photo" role="img" aria-label="Photo of a videographer crouching with a professional video camera"></div>
  <div class="experience-banner">Over 15 Years of Legal Video Experience</div>
  <h1 class="service-title">LEGAL<br>VIDEO<br>SERVICES</h1>
  <ul class="service-list">
    <li>Expert &amp; Lay Witness Depositions</li>
    <li>Day in the Life Videos</li>
    <li>Security &amp; Surveillance Video Editing</li>
    <li>Onsite Video Documentation</li>
    <li>Ability to make bad video clearer</li>
    <li>Focus Groups &amp; Video Monitoring</li>
    <li>Video Conversion and Duplication</li>
  </ul>
  <div class="front-contacts">
    <span class="contact">
      <svg viewBox="0 0 16 16" aria-hidden="true"><circle cx="8" cy="8" r="7" fill="none" stroke="#fff" stroke-width="1.2"/><path d="M5.5 4.5l1.4 1.6-.8 1a5 5 0 0 0 2.8 2.8l1-.8 1.6 1.4-.9 1.1c-3 0-6.1-3.1-6.1-6.1z" fill="#fff"/></svg>
      418.562.7391
    </span>
    <span class="contact">
      <svg viewBox="0 0 16 16" aria-hidden="true"><circle cx="8" cy="8" r="7" fill="none" stroke="#fff" stroke-width="1.2"/><rect x="4" y="5.5" width="8" height="5.5" fill="none" stroke="#fff"/><path d="M4 5.5l4 3 4-3" fill="none" stroke="#fff"/></svg>
      Walter@Carlvista.example
    </span>
  </div>
</section>

<section class="postcard postcard--back" aria-label="Postcard mailing side">
  <div class="back-banner">LEGAL VIDEO SERVICES</div>
  <address class="return-address">
    <span class="return-name">Carlvista</span><br>
    Lakemont, MN 55912<br>
    United States
  </address>
  <div class="stamp-box" aria-label="Stamp area"></div>
  <div class="logo-mark"><span class="dot"></span>Carlvista</div>
  <div class="grey-band">
    <span class="band-name">Carlvista</span>
    <div class="band-contacts">
      <div>418.562.7391</div>
      <div>Walter@Carlvista.example</div>
    </div>
  </div>
  <div class="web-band">www.carlvista.example</div>
  <div class="address-lines" aria-label="Recipient address lines">
    <span></span><span></span><span></span><span></span><span></span><span></span>
  </div>
</section>

</body>
</html>
```